Solar appointment reminder card

We are looking for a new design for our appointment reminder card since we have changed our logo. The card should have the new logo along with space for the employee to hand write the customers appointment date, time, the employees name and phone number.
I've uploaded what our old basic appointment card looked like and our new logo.

The cards should be in a standard business card size and could be horizontal or vertical.

```html
<!DOCTYPE html>
<html lang="en">
<head>
<meta charset="utf-8">
<title>Sunward Solar – Appointment Card</title>
<link rel="stylesheet" href="https://fonts.googleapis.com/css2?family=Lato:wght@400;700&display=swap">
<style>
  :root {
    --backdrop: #f3ead2;
    --card: #fbfbfa;
    --orange: #ef8a1c;
    --yellow: #f4bf1a;
    --icon-soft: #fbe3c4;
  }
  html, body {
    margin: 0;
    padding: 0;
    width: 1200px;
    height: 900px;
    overflow: hidden;
    background: var(--backdrop);
    font-family: "Lato", sans-serif;
  }
  .stage {
    width: 1200px;
    height: 900px;
    display: flex;
    align-items: center;
    justify-content: center;
  }
  .card {
    position: relative;
    width: 980px;
    height: 554px;
    background: var(--card);
    box-sizing: border-box;
    border-top: 13px solid var(--orange);
    border-bottom: 13px solid var(--orange);
    border-left: 11px solid var(--yellow);
    border-right: 11px solid var(--yellow);
    box-shadow: 0 10px 30px rgba(0,0,0,0.08);
  }
  .brand {
    position: absolute;
    left: 130px;
    top: 205px;
    display: flex;
    align-items: center;
    gap: 18px;
  }
  .brand-dot {
    width: 64px;
    height: 64px;
    border-radius: 50%;
    background: var(--yellow);
    flex: none;
  }
  .brand-name {
    color: var(--orange);
    font-weight: 700;
    font-size: 42px;
    line-height: 1.0;
    letter-spacing: 1px;
  }
  .appointment {
    position: absolute;
    left: 540px;
    top: 118px;
  }
  .appointment-title {
    display: inline-block;
    margin: 0 0 28px 60px;
    color: var(--orange);
    font-weight: 700;
    font-size: 36px;
    letter-spacing: 0.5px;
    padding-bottom: 4px;
    border-bottom: 6px solid var(--yellow);
  }
  .fields {
    list-style: none;
    margin: 0;
    padding: 0;
  }
  .field {
    display: flex;
    align-items: center;
    height: 72px;
  }
  .field-icon {
    width: 46px;
    height: 46px;
    flex: none;
    margin-right: 26px;
  }
  .field-icon.person {
    border-radius: 8px;
    background: var(--icon-soft);
  }
  .field-label {
    color: var(--yellow);
    font-weight: 400;
    font-size: 34px;
    letter-spacing: 0.5px;
  }
</style>
</head>
<body>
<main class="stage">
  <section class="card">
    <div class="brand">
      <span class="brand-dot"></span>
      <span class="brand-name">SUNWARD<br>SOLAR</span>
    </div>

    <div class="appointment">
      <h1 class="appointment-title">APPOINTMENT</h1>
      <ul class="fields">
        <li class="field">
          <svg class="field-icon" viewBox="0 0 46 46" fill="none" stroke="var(--orange)" stroke-width="2">
            <rect x="4" y="8" width="38" height="34" rx="2"/>
            <line x1="4" y1="17" x2="42" y2="17"/>
            <line x1="13" y1="4" x2="13" y2="11"/>
            <line x1="33" y1="4" x2="33" y2="11"/>
            <g fill="var(--orange)" stroke="none">
              <circle cx="12" cy="24" r="1.4"/><circle cx="19" cy="24" r="1.4"/><circle cx="26" cy="24" r="1.4"/><circle cx="33" cy="24" r="1.4"/>
              <circle cx="12" cy="30" r="1.4"/><circle cx="19" cy="30" r="1.4"/><circle cx="26" cy="30" r="1.4"/><circle cx="33" cy="30" r="1.4"/>
              <circle cx="12" cy="36" r="1.4"/><circle cx="19" cy="36" r="1.4"/><circle cx="26" cy="36" r="1.4"/>
            </g>
          </svg>
          <span class="field-label">DATE:</span>
        </li>
        <li class="field">
          <svg class="field-icon" viewBox="0 0 46 46" fill="none" stroke="var(--orange)" stroke-width="2">
            <circle cx="23" cy="23" r="19"/>
            <circle cx="23" cy="23" r="15"/>
            <polyline points="23,13 23,24 30,24"/>
          </svg>
          <span class="field-label">TIME:</span>
        </li>
        <li class="field">
          <span class="field-icon person" role="img" aria-label="Representative icon"></span>
          <span class="field-label">REPRESENTATIVE:</span>
        </li>
        <li class="field">
          <svg class="field-icon" viewBox="0 0 46 46" fill="none" stroke="var(--orange)" stroke-width="2" stroke-linejoin="round">
            <path d="M12 5 L18 13 L15 18 Q19 28 28 33 L33 30 L41 36 L37 42 Q22 42 12 30 Q5 20 7 9 Z"/>
          </svg>
          <span class="field-label">PHONE:</span>
        </li>
      </ul>
    </div>
  </section>
</main>
</body>
</html>
```